I need a simple, classy and stylish business card. I would like it to have a black background with white writing. I would like you to use my logo you designed on the front with the word 'Imagery" used underneath it in the same font. On the back I was thinking of the website at the top 'tomverrick.com' Then my social media accounts, Can you use the instagram, Facebook and twitter logo then my handles?
Please let me know what you think.
Regards Tom
Must have
- Website: www.tomverrick.com
- Social media handles..
- Instagram: @Tom_Verrick_Imagery
- Facebook: Tom Verrick Imagery
- Twitter: @Tom_Verrick
- Email: info@tomverick.com
- Phone: 0437 518 293

```html
<!DOCTYPE html>
<html lang="en">
<head>
<meta charset="utf-8">
<title>Tom Verrick Imagery – Business Card</title>
<link rel="stylesheet" href="https://fonts.googleapis.com/css2?family=Indie+Flower&family=Arimo:wght@400;700&display=swap">
<style>
  :root {
    --page: #e9e6e2;
    --card-black: #0b0b0b;
    --card-sheen: #262626;
    --stripe: #1c1c1c;
    --ink-white: #ffffff;
    --ink-black: #0a0a0a;
    --script: "Indie Flower", cursive;
    --sans: "Arimo", Arial, sans-serif;
  }
  * { margin: 0; padding: 0; box-sizing: border-box; }
  html, body {
    width: 1200px; height: 913px; overflow: hidden;
    background: var(--page);
  }
  .sheet {
    position: relative; width: 1200px; height: 913px;
    display: flex; align-items: center; justify-content: center; gap: 40px;
  }
  .card {
    position: relative; width: 540px; height: 309px;
    background: linear-gradient(120deg, var(--card-black) 0%, var(--card-sheen) 48%, var(--card-black) 70%);
    overflow: hidden;
    box-shadow: 0 10px 24px rgba(0,0,0,.25);
  }
  .card__shapes { position: absolute; inset: 0; }

  /* contact side */
  .logo-line {
    position: absolute; top: 16px; right: 44px;
    display: flex; align-items: center; gap: 10px;
    color: var(--ink-white); font-family: var(--script); font-size: 28px; line-height: 1;
    white-space: nowrap;
  }
  .logo-line__dot { width: 22px; height: 22px; border: 2px solid var(--ink-white); border-radius: 50%; }
  .person {
    position: absolute; left: 34px; top: 160px; color: var(--ink-black); font-family: var(--sans);
    white-space: nowrap;
  }
  .person__name { font-size: 19px; font-weight: 700; }
  .person__role { font-size: 12px; padding-left: 60px; margin-top: 1px; }
  .contacts {
    position: absolute; right: 22px; top: 72px; list-style: none;
    font-family: var(--sans); font-size: 13.5px; color: var(--ink-black);
    white-space: nowrap;
  }
  .contacts li { display: flex; justify-content: flex-end; align-items: center; gap: 7px; height: 19px; }
  .contacts .icon { width: 13px; height: 13px; flex: none; }
  .tagline {
    position: absolute; left: 120px; bottom: 22px;
    color: var(--ink-white); font-family: var(--script); font-size: 30px;
  }

  /* logo side */
  .brand {
    position: absolute; left: 50%; top: 50%; transform: translate(-50%, -50%);
    display: flex; align-items: flex-end; gap: 16px; color: var(--ink-white);
    white-space: nowrap;
  }
  .brand__dot { width: 56px; height: 56px; border: 3px solid var(--ink-white); border-radius: 50%; flex: none; margin-bottom: 4px; }
  .brand__name { font-family: var(--script); font-size: 50px; line-height: 1; }
  .brand__sub { font-family: var(--script); font-size: 38px; line-height: 1.1; padding-left: 60px; }
</style>
</head>
<body>
<main class="sheet">

  <section class="card card--contact" aria-label="Contact side">
    <svg class="card__shapes" viewBox="0 0 540 309" aria-hidden="true">
      <polygon points="0,100 230,18 330,18 90,100" fill="var(--stripe)"/>
      <polygon points="300,309 540,215 540,260 400,309" fill="var(--stripe)"/>
      <polygon points="0,148 200,148 285,64 540,64 540,200 318,200 230,248 0,248" fill="var(--ink-white)"/>
    </svg>

    <div class="logo-line"><span class="logo-line__dot"></span>Tom Verrick</div>

    <div class="person">
      <p class="person__name">Alex Morgan</p>
      <p class="person__role">Designation</p>
    </div>

    <ul class="contacts">
      <li>0437 518 293
        <svg class="icon" viewBox="0 0 14 14"><circle cx="7" cy="7" r="7" fill="var(--ink-black)"/><path d="M4.2 3.6l1.4-.3.8 1.9-.9.7c.5 1 1.2 1.7 2.2 2.2l.7-.9 1.9.8-.3 1.4c-3 .2-6-2.8-5.8-5.8z" fill="var(--ink-white)"/></svg></li>
      <li>info@tomverick.com
        <svg class="icon" viewBox="0 0 14 14"><circle cx="7" cy="7" r="7" fill="var(--ink-black)"/><rect x="3.5" y="4.5" width="7" height="5" fill="none" stroke="var(--ink-white)" stroke-width="1"/><path d="M3.5 4.5l3.5 2.8 3.5-2.8" fill="none" stroke="var(--ink-white)" stroke-width="1"/></svg></li>
      <li>www.tomverrick.com
        <svg class="icon" viewBox="0 0 14 14"><circle cx="7" cy="7" r="7" fill="var(--ink-black)"/><circle cx="7" cy="7" r="4.3" fill="none" stroke="var(--ink-white)" stroke-width="1"/><path d="M2.7 7h8.6M7 2.7v8.6" stroke="var(--ink-white)" stroke-width="1"/></svg></li>
      <li>@Tom_Verrick_Imagery
        <svg class="icon" viewBox="0 0 14 14"><circle cx="7" cy="7" r="7" fill="var(--ink-black)"/></svg></li>
      <li>@TomVerrickImagery
        <svg class="icon" viewBox="0 0 14 14"><circle cx="7" cy="7" r="7" fill="var(--ink-black)"/></svg></li>
      <li>@Tom_Verrick
        <svg class="icon" viewBox="0 0 14 14"><circle cx="7" cy="7" r="7" fill="var(--ink-black)"/></svg></li>
    </ul>

    <p class="tagline">Imagery</p>
  </section>

  <section class="card card--brand" aria-label="Logo side">
    <div class="brand">
      <span class="brand__dot"></span>
      <div>
        <p class="brand__name">Tom Verrick</p>
        <p class="brand__sub">Imagery</p>
      </div>
    </div>
  </section>

</main>
</body>
</html>
```